Designs für LED-Wände
Zielgruppe
ORTB ist ein Beratungsunternehmen im Bereich Information- und Content-Management. Wir unterstützen bei der Auswahl, Einführung und Betreuung unterschiedlichster Systemlösungen. Unser Ziel ist es, Informationsflüsse reibungslos zu gestalten, indem wir gemeinsam mit unseren Kunden ihre Informationslandschaft analysieren und optimieren. Dabei bringen wir Know-how zu Tools, Methoden und Strategien ein.
Aufgabenstellung
Siehe Anhang 'Design-Briefing'

```html
<!DOCTYPE html>
<html lang="de">
<head>
<meta charset="utf-8">
<title>ORTB – LED-Wand Motive</title>
<link href="https://fonts.googleapis.com/css2?family=Roboto:wght@400;700&display=swap" rel="stylesheet">
<style>
  :root {
    --slate: #4a5f68;
    --green: #9bc31f;
    --white: #ffffff;
    --panel-tint: #eef1f3;
    --stage: #e9ebee;
  }
  html, body {
    margin: 0;
    width: 1162px;
    height: 1200px;
    overflow: hidden;
    background: var(--stage);
    font-family: "Roboto", Arial, sans-serif;
  }
  .wall {
    position: absolute;
    top: 344px;
    height: 512px;
    background: linear-gradient(160deg, var(--white) 30%, var(--panel-tint) 100%);
    overflow: hidden;
  }
  .wall-cover { left: 100px; width: 377px; }
  .wall-services { left: 501px; width: 562px; }

  .stripe-backdrop {
    position: absolute;
    inset: 0;
    background: linear-gradient(135deg, rgba(255,255,255,0) 40%, rgba(228,232,235,0.6) 100%);
  }

  /* cover panel */
  .brand-bar {
    position: absolute;
    left: 40px; top: 46px;
    width: 285px; height: 31px;
    background: var(--green);
    display: flex; align-items: center;
    color: var(--white);
    font-weight: 700;
  }
  .brand-name { font-size: 24px; margin-left: 12px; letter-spacing: 0.5px; }
  .brand-divider { width: 3px; height: 31px; background: var(--white); margin: 0 10px 0 12px; }
  .brand-partner { font-size: 10px; display: flex; align-items: center; gap: 4px; }
  .brand-partner .dot { width: 7px; height: 7px; border-radius: 50%; background: var(--white); }
  .brand-rules { position: absolute; left: 40px; top: 81px; width: 285px; }
  .brand-rules span { display: block; background: var(--green); }

  .headline {
    position: absolute;
    left: 38px; top: 122px;
    margin: 0;
    font-size: 40px;
    line-height: 43px;
    font-weight: 700;
    letter-spacing: 0.3px;
  }
  .headline .dark { color: var(--slate); display: block; }
  .headline .accent { color: var(--green); display: block; }

  .partners {
    position: absolute;
    left: 40px; top: 332px;
    width: 310px;
    display: flex; flex-wrap: wrap;
    column-gap: 20px; row-gap: 14px;
    align-items: center;
    color: var(--slate);
  }
  .partner { display: flex; align-items: center; gap: 4px; font-size: 10px; font-weight: 400; }
  .partner .mark { width: 10px; height: 10px; border-radius: 50%; background: var(--slate); }
  .partner.large { font-size: 16px; }
  .partner.bold { font-size: 12px; font-weight: 700; }

  /* services panel */
  .band { position: absolute; top: 0; bottom: 0; background: var(--green); }
  .services {
    position: absolute;
    left: 113px; top: 108px;
    margin: 0; padding: 0;
    list-style: none;
  }
  .service {
    display: flex; align-items: center;
    height: 30px;
    margin-bottom: 33.5px;
    font-size: 19px;
    color: var(--slate);
    letter-spacing: 0.1px;
  }
  .service svg { width: 30px; height: 30px; margin-right: 18px; flex: none; }
  .service .hl { color: var(--green); }
</style>
</head>
<body>

<section class="wall wall-cover">
  <div class="stripe-backdrop" role="img" aria-label="Dezentes diagonales Streifenmuster in Hellgrau"></div>

  <div class="brand-bar">
    <span class="brand-name">ORTB</span>
    <span class="brand-divider"></span>
    <span class="brand-partner"><span class="dot"></span>Vernalo</span>
  </div>
  <div class="brand-rules">
    <span style="height:4px;margin-bottom:3px"></span>
    <span style="height:3px;margin-bottom:4px"></span>
    <span style="height:2px;margin-bottom:5px"></span>
    <span style="height:1px;margin-bottom:5px"></span>
    <span style="height:1px;opacity:.6"></span>
  </div>

  <h1 class="headline">
    <span class="dark">UNABHÄNGIGE</span>
    <span class="accent">BERATUNG</span>
    <span class="dark">INDIVIDUELLE</span>
    <span class="accent">LÖSUNGEN</span>
  </h1>

  <div class="partners">
    <span class="partner"><span class="mark"></span>Tarnwick Notes</span>
    <span class="partner"><span class="mark"></span>lumidrax</span>
    <span class="partner">SORVELT</span>
    <span class="partner large">Pelmora</span>
    <span class="partner"><span class="mark"></span>Halden Relay Systems</span>
    <span class="partner bold">KLEFTA</span>
    <span class="partner"><span class="mark"></span>vbm</span>
  </div>
</section>

<section class="wall wall-services">
  <div class="stripe-backdrop" role="img" aria-label="Dezentes diagonales Streifenmuster in Hellgrau"></div>

  <span class="band" style="left:0;width:39px"></span>
  <span class="band" style="left:45px;width:6px"></span>
  <span class="band" style="left:57px;width:5px"></span>
  <span class="band" style="left:66px;width:4px"></span>
  <span class="band" style="left:73px;width:2px"></span>
  <span class="band" style="left:77px;width:1px"></span>

  <ul class="services">
    <li class="service">
      <svg viewBox="0 0 30 30" aria-hidden="true">
        <circle cx="15" cy="15" r="11" fill="var(--slate)"/>
        <ellipse cx="15" cy="15" rx="14" ry="6" fill="none" stroke="var(--green)" stroke-width="1.6" transform="rotate(-35 15 15)"/>
        <circle cx="15" cy="2" r="2" fill="var(--green)"/>
        <circle cx="15" cy="28" r="2" fill="var(--green)"/>
      </svg>
      <span>KNOWLEDGE <span class="hl">GRAPH</span></span>
    </li>
    <li class="service">
      <svg viewBox="0 0 30 30" aria-hidden="true" fill="none" stroke="var(--slate)" stroke-width="1.6">
        <rect x="2" y="3" width="11" height="8"/>
        <rect x="17" y="19" width="11" height="8"/>
        <path d="M13 7h8v8M9 11v12h8" stroke="var(--green)" stroke-dasharray="2 2"/>
        <circle cx="27" cy="10" r="1.8" fill="var(--slate)"/>
        <circle cx="3" cy="27" r="1.8" fill="var(--slate)"/>
      </svg>
      <span><span class="hl">DIGITAL</span> INFORMATION TWIN</span>
    </li>
    <li class="service">
      <svg viewBox="0 0 30 30" aria-hidden="true">
        <g stroke="var(--slate)" stroke-width="3">
          <path d="M15 5v20M5 15h20M8 8l14 14M22 8L8 22"/>
        </g>
        <circle cx="15" cy="15" r="7" fill="var(--slate)"/>
        <circle cx="15" cy="15" r="3" fill="var(--green)"/>
        <path d="M15 0v3M15 27v3M0 15h3M27 15h3" stroke="var(--green)" stroke-width="1.5"/>
      </svg>
      <span>SYSTEM OPTIMIZATION AND <span class="hl">AUTOMATION</span></span>
    </li>
    <li class="service">
      <svg viewBox="0 0 30 30" aria-hidden="true">
        <rect x="3" y="8" width="24" height="16" fill="none" stroke="var(--slate)" stroke-width="1.6"/>
        <rect x="6" y="11" width="18" height="10" fill="var(--slate)"/>
        <path d="M10 20v-5M14 20v-7M18 20v-4" stroke="var(--green)" stroke-width="1.6"/>
        <path d="M1 26h28" stroke="var(--slate)" stroke-width="2"/>
        <path d="M12 8V3h8v5" fill="none" stroke="var(--green)" stroke-width="1.2"/>
      </svg>
      <span>AGILE <span class="hl">PROJECT</span> MANAGEMENT</span>
    </li>
    <li class="service">
      <svg viewBox="0 0 30 30" aria-hidden="true">
        <rect x="4" y="4" width="22" height="17" fill="var(--slate)"/>
        <rect x="7" y="7" width="16" height="11" fill="var(--white)"/>
        <path d="M10 17v-4M13 17v-6M16 17v-3M19 17v-7" stroke="var(--green)" stroke-width="1.8"/>
        <path d="M1 24h28l-2 3H3z" fill="var(--green)"/>
      </svg>
      <span><span class="hl">BUSINESS</span> DATA ANALYTICS</span>
    </li>
  </ul>
</section>

</body>
</html>
```